Lindenfall Studio Business cards

Design our business cards and eventually a logo. The company is based in Paris, its activity is the retailing via internet of luxury home furniture (like Vantorelli, Bercasso, fradusi...) Our clients are international andwith a high sense of aesthetics. The design shall communicate wealth and trust with a high quality and aesthetic sense, pure lines Company Name is Lindenfall StudioExplanation of the name: usually people who wants to buy furniture usually go in a showroom. Today they go in showroom to test the furniture and they search for the price on internet, which is a "Lindenfall studio".We will not be a e-commerce site. Our site will be (another project) a presentation site which purpose is to reach qualified prospects. Then everything will be handled by phone, meeting etc.The business card must be professional as we will negotiate with many luxury brands, opportunity to represent them on our site, prices etc.As far as the color are concerned mostly black and whithe or grey. The font of the Lindenfall Studio name shall have some impact.

Target Market(s)

High-end furniture and buyers of luxury goods, international customers, mostly women who handle such projects.
We also deal with professional buyers (hotels as an example) and luxury brands

Contact Information for Business Card

standard format 85x55, lanscape card, square corners will be printed on thick high quality paper (300 or 350g)

Font styles to use
Sans Serif

Colors

Designer to choose colors to be used in the design.

Requirements
Must have
• Must be white, as the paper will be high quality, the paper will enhance the card.
• Name of the brand Lindenfall studio (with specific font which make it very nice looking and catch the attention. similar to Calibri or Calibri
• Name of person (will give you the name later (4 names and position)
• the position of the person
• Mobile phone, e-mail, Physical address 27, rue Caldenois, 75005 Paris, France (courrier only) our web site www.lindenfallstudio-example.fr
• The card must be simple and class
Nice to have
• Font of the address is smaller than the rest,
• Calibri font or similar on recto side with the name of the company which may look similar to the picture inserted in the brief.
• The grey color in the picture inserted is ok for us
Should not have
• Any parallel lines which represent the name of the company
• Any heavy design If you go on internet sites which present the furniture all designs are pure lines and high quality craftsmanship. To have an idea of our targetted client or brand we will be in touch: https://www.casavornetta-example.it/projects/
• Note that the picture added below is what we use, now as mail signature, up to you to have a better design etc.

```html
<!DOCTYPE html>
<html lang="en">
<head>
<meta charset="utf-8">
<title>Lindenfall Studio – Business Cards</title>
<link href="https://fonts.googleapis.com/css2?family=Carlito:wght@400;700&family=Open+Sans:wght@400;600&family=PT+Serif:ital@1&display=swap" rel="stylesheet">
<style>
  :root {
    --backdrop: #e9e7e4;
    --paper: #eeeeec;
    --ink: #4a4a4a;
    --ink-soft: #5c5c5c;
    --card-dark: #2c2c2c;
    --ink-light: #f4f4f2;
  }
  * { margin: 0; padding: 0; box-sizing: border-box; }
  html, body {
    width: 1200px;
    height: 672px;
    overflow: hidden;
    background: var(--backdrop);
  }
  .sheet {
    width: 1200px;
    height: 672px;
    display: flex;
    align-items: center;
    justify-content: center;
    gap: 60px;
  }
  .card {
    width: 480px;
    height: 310px;
    position: relative;
    box-shadow: 0 6px 18px rgba(0,0,0,0.12);
  }
  .card--front { background: var(--paper); color: var(--ink); }
  .card--back { background: var(--card-dark); color: var(--ink-light); }

  .company-name {
    font-family: "Carlito", "Calibri", sans-serif;
    font-variant: small-caps;
    font-weight: 700;
    letter-spacing: 0.06em;
  }
  .card--front .company-name {
    position: absolute;
    left: 44px;
    top: 168px;
    font-size: 21px;
  }

  .contact {
    position: absolute;
    left: 258px;
    top: 96px;
    font-family: "Open Sans", sans-serif;
    font-size: 13px;
    line-height: 1.45;
    color: var(--ink-soft);
  }
  .contact__name {
    font-size: 17px;
    font-weight: 600;
    color: var(--ink);
    line-height: 1.2;
  }
  .contact__role {
    font-family: "PT Serif", serif;
    font-style: italic;
    font-size: 13px;
    margin-bottom: 10px;
  }
  .contact__line {
    display: flex;
    align-items: flex-start;
    gap: 8px;
  }
  .contact__icon {
    width: 11px;
    height: 11px;
    margin-top: 4px;
    flex: none;
    fill: var(--ink-soft);
  }
  .contact__address { font-size: 12px; }

  .card--back .brand-lockup {
    position: absolute;
    inset: 0;
    display: flex;
    flex-direction: column;
    align-items: center;
    justify-content: center;
    gap: 22px;
  }
  .brand-mark {
    width: 14px;
    height: 14px;
    background: var(--ink-light);
  }
  .card--back .company-name { font-size: 31px; }
</style>
</head>
<body>
  <main class="sheet">
    <section class="card card--front" aria-label="Business card front">
      <p class="company-name">Lindenfall Studio SAS</p>
      <div class="contact">
        <p class="contact__name">Mathis Orvalle</p>
        <p class="contact__role">Président and Co-Founder</p>
        <p class="contact__line">
          <svg class="contact__icon" viewBox="0 0 12 12" aria-hidden="true"><path d="M2.5 0.5h2l1 3-1.4 1a7 7 0 0 0 3.4 3.4l1-1.4 3 1v2a1.5 1.5 0 0 1-1.5 1.5A9.5 9.5 0 0 1 1 2 1.5 1.5 0 0 1 2.5 0.5z"/></svg>
          <span>+33612480937</span>
        </p>
        <p class="contact__line contact__address">
          <svg class="contact__icon" viewBox="0 0 12 12" aria-hidden="true"><path d="M6 0.5a4 4 0 0 0-4 4c0 3 4 7 4 7s4-4 4-7a4 4 0 0 0-4-4zm0 5.6a1.6 1.6 0 1 1 0-3.2 1.6 1.6 0 0 1 0 3.2z"/></svg>
          <span>27 rue Caldenois<br>75005 Paris, France</span>
        </p>
      </div>
    </section>

    <section class="card card--back" aria-label="Business card back">
      <div class="brand-lockup">
        <span class="brand-mark" aria-hidden="true"></span>
        <p class="company-name">Lindenfall Studio SAS</p>
      </div>
    </section>
  </main>
</body>
</html>
```